Black Granite Web Design Project

We are looking for a design for a new company that will be selling Black Granite slabs and tiles. We will be selling to both end-consumers and granite installers. We have already settled on a logo and hopefully this will give an idea of what we like in our designs. We are not going to be selling online but want people to call us so the site is basically an enhanced business card. We will be focusing a lot on SEO so the design will have to keep that in mind.

We would like to keep the design in 1024x768 to make it easily view-able on all devices.

Regarding navigation there should only be a few sub-pages, like "Granite Slabs", "Granite Tiles", "Delivery", "Contact"

Aside from that we are open to designs. One idea we did have was to personalize the site and have a person there somehow to represent the company, making the user feel there are real people behind this site. This is just an idea and not a must.

The name of the company and site is "Silver Brook Petrano"

Thanks
Updates

Hello All,

Thanks for the great designs. There are some good looking designs that show beautiful kitchens but this site is made for the granite installers and not the retail consumers. So in order not to to confuse the buyers I would like to keep this as much about the raw products as possible. The raw products being the granite slabs, thereby making it obvious we don't sell granite counter tops. 

This design will really be the identity of this company so it is important we get the right message across on this index page and that this page is as complete as possible.

Again, thanks for all the work being put into this.

Target Market(s)

The target audience is granite installers or companies that would with granite slabs.

Industry/Entity Type

Business

```html
<!DOCTYPE html>
<html lang="en">
<head>
<meta charset="utf-8">
<title>Silver Brook Petrano</title>
<link href="https://fonts.googleapis.com/css2?family=Arimo:wght@400;700&display=swap" rel="stylesheet">
<style>
:root{
  --paper:#efefef;
  --band:#e2e2e2;
  --ink:#1c1c1c;
  --muted:#8a8a8a;
  --dark:#262626;
  --nav:#3a3a3a;
  --green:#3fae2a;
  --link:#2f8f22;
  --white:#ffffff;
  --field:#2f2d2c;
}
*{margin:0;padding:0;box-sizing:border-box}
html,body{width:777px;height:1200px;overflow:hidden}
body{position:relative;background:var(--paper);font-family:"Arimo",Arial,sans-serif;color:var(--ink);font-size:9px;line-height:1.45}
.abs{position:absolute}
a{text-decoration:none}

/* header */
.site-header{left:0;top:0;width:777px;height:75px;background:linear-gradient(#f6f6f6,#e6e6e6)}
.brand{left:70px;top:22px;display:flex;align-items:center;gap:6px}
.brand-mark{width:52px;height:26px;background:var(--ink)}
.brand-rule{width:1px;height:30px;background:var(--ink)}
.brand-name{font-weight:700;font-size:12px;letter-spacing:-.3px;line-height:1.1;white-space:nowrap}
.brand-place{font-size:7px;letter-spacing:.6px;white-space:nowrap}
.main-nav{left:297px;top:23px;width:415px;height:26px;background:linear-gradient(#4a4a4a,#2e2e2e);border-radius:4px;display:flex;align-items:center;padding-left:14px;white-space:nowrap}
.main-nav a{color:var(--white);font-weight:700;font-size:8px;padding:0 8px;height:22px;line-height:22px;white-space:nowrap}
.main-nav a.current{background:var(--green)}

/* hero */
.hero{left:0;top:75px;width:777px;height:305px;background:var(--dark)}
.hero-photo{left:63px;top:75px;width:647px;height:305px;background:linear-gradient(160deg,#c9c6bd 0%,#a19c90 40%,#6a675f 75%,#3a3935 100%)}
.hero-caption{left:63px;top:345px;width:647px;height:35px;background:rgba(40,40,40,.7);color:var(--white)}
.hero-caption h1{position:absolute;left:45px;top:8px;font-size:16px;font-weight:700;white-space:nowrap}
.hero-caption p{position:absolute;left:325px;top:6px;width:270px;font-size:8.5px;line-height:1.35}
.arrow{top:355px}

/* intro */
.section-title{font-weight:700;font-size:10px;letter-spacing:.2px;white-space:nowrap}
.intro-photo{left:79px;top:430px;width:176px;height:89px;background:linear-gradient(#b9b3a8,#8f887c)}
.intro-text{left:266px;top:428px;width:195px;color:var(--muted);font-size:8px}
.more{left:266px;top:510px;font-weight:700;font-size:8.5px;color:var(--ink)}
.why-text{left:79px;top:552px;width:385px;color:var(--muted);font-size:8px}
.delivery-text{color:var(--muted);font-size:8px}
.check{left:489px;top:532px;font-size:8px;font-weight:700;color:#555;white-space:nowrap}

/* products */
.products{left:0;top:594px;width:777px;height:299px;background:var(--band)}
.products-title{left:0;top:610px;width:777px;text-align:center;font-size:12px;font-weight:700;letter-spacing:.4px}
.card{top:645px;width:176px;height:224px;background:var(--white);text-align:center}
.card-photo{height:120px}
.card h3{font-size:9px;font-weight:700;margin-top:14px}
.card p{font-size:8px;color:#555;margin:8px 12px 0}
.card a{display:block;margin-top:12px;color:var(--link);font-size:8.5px}

/* clients */
.clients{left:0;top:893px;width:777px;height:102px;background:linear-gradient(#e8e8e8,#dcdcdc)}
.client{font-weight:700;font-size:12px;color:#444;white-space:nowrap}
.cert-badge{width:38px;height:38px;border-radius:50%;border:2px solid #333}

/* footer */
.site-footer{left:0;top:995px;width:777px;height:168px;background:var(--white)}
.foot-head{font-weight:700;font-size:9px;letter-spacing:.3px}
.foot-list{list-style:none;font-size:8.5px;line-height:16.5px}
.foot-list a{color:var(--ink)}
.foot-list a.current{color:var(--green)}
.products-list a{color:#555}
.field{width:137px;height:25px;background:var(--field);border-radius:3px;color:#ddd;font-size:7.5px;padding:7px 6px}
.submit{left:660px;top:1119px;font-weight:700;font-size:9px}
.bottom-bar{left:0;top:1163px;width:777px;height:37px;background:var(--dark);color:#aaa;font-size:8px;line-height:1.3;padding:6px 0 0 96px}
.social{top:1170px;width:20px;height:20px;border-radius:50%}
</style>
</head>
<body>

<header class="site-header abs">
  <div class="brand abs">
    <div class="brand-mark"></div>
    <div class="brand-rule"></div>
    <div>
      <div class="brand-name">SILVER BROOK PETRANO</div>
      <div class="brand-place">VALE SERRANO</div>
    </div>
  </div>
  <nav class="main-nav abs">
    <a class="current" href="#">HOME</a><a href="#">ABOUT US</a><a href="#">GRANITE SLABS</a><a href="#">GRANITE TILES</a><a href="#">DELIVERY</a><a href="#">CONTACT US</a>
  </nav>
</header>

<section>
  <div class="hero abs"></div>
  <div class="hero-photo abs" role="img" aria-label="Photograph of weathered pale granite boulders streaked with dark lichen"></div>
  <div class="hero-caption abs">
    <h1>GRANITE IN ITS PUREST FORM</h1>
    <p>Sed ut perspiciatis unde omnis iste natus error sit voluptatem accusantium doloremque laudantium</p>
  </div>
  <svg class="arrow abs" style="left:82px" width="12" height="16" viewBox="0 0 12 16"><path d="M10 1 3 8l7 7" fill="none" stroke="#ccc" stroke-width="3"/></svg>
  <svg class="arrow abs" style="left:682px" width="12" height="16" viewBox="0 0 12 16"><path d="M2 1l7 7-7 7" fill="none" stroke="#ccc" stroke-width="3"/></svg>
</section>

<section>
  <h2 class="section-title abs" style="left:78px;top:411px">WELCOME TO SILVER BROOK PETRANO</h2>
  <div class="intro-photo abs" role="img" aria-label="Photograph of a warehouse stocked with granite slabs"></div>
  <p class="intro-text abs">Sed ut perspiciatis unde omnis iste natus error sit volup tatem accusantium doloremque laudantium, totam rem eaque ipsa quae ab illo inventore veritatis et quasi arch itecto beatae vitae dicta sunt explicabo. Nemo enim ip voluptatem quia voluptas sit aspernatur aut odit aut fug it, sed quia consequuntur magni dolores eos qui ration voluptatem sequi nesciunt</p>
  <a class="more abs" href="#">Know more about us</a>
  <h2 class="section-title abs" style="left:78px;top:537px">WHY CHOOSE US?</h2>
  <p class="why-text abs">Sed ut perspiciatis unde omnis iste natus error sit volup tatem accusantium doloremque laudantium, totam rem eaque ipsa quae ab</p>

  <h2 class="section-title abs" style="left:486px;top:396px;font-size:8.5px">DELIVERY AT YOUR LOCATION</h2>
  <p class="delivery-text abs" style="left:486px;top:429px;width:215px">Sed ut perspiciatis unde omnis iste natus error sit voluptatem accusantium doloremque laudantium, totam rem eaque ipsa quae ab illo</p>
  <svg class="abs" style="left:486px;top:471px" width="52" height="44" viewBox="0 0 52 44">
    <circle cx="13" cy="13" r="11" fill="none" stroke="#111" stroke-width="3"/>
    <path d="M13 6v7l5 3" stroke="#111" stroke-width="2.5" fill="none"/>
    <rect x="14" y="20" width="22" height="16" fill="#111"/>
    <path d="M37 23h7l6 7v6H37z" fill="#111"/>
    <circle cx="21" cy="38" r="4" fill="#111" stroke="#efefef" stroke-width="2"/>
    <circle cx="43" cy="38" r="4" fill="#111" stroke="#efefef" stroke-width="2"/>
  </svg>
  <p class="delivery-text abs" style="left:552px;top:483px;width:150px">Sed ut perspiciatis unde omnis iste natus error sit voluptatem</p>
  <a class="check abs" href="#">CLICK HERE TO CHECK YOUR LOCATION</a>
</section>

<section>
  <div class="products abs"></div>
  <h2 class="products-title abs">OUR TOP RANGE PRODUCTS</h2>
  <article class="card abs" style="left:92px">
    <div class="card-photo" role="img" aria-label="Close-up of speckled brown and grey granite" style="background:linear-gradient(135deg,#8a6d62,#5e5350,#9a8a84)"></div>
    <h3>GRANITE PRE FABS</h3>
    <p>Sed ut perspiciatis unde omnis iste natus error sit voluptatem accusantium doloremq ue laudantium, totam rem eaque ipsa quae ab illo inventore veritatis</p>
    <a href="#">Read more &nbsp;»</a>
  </article>
  <article class="card abs" style="left:300px">
    <div class="card-photo" role="img" aria-label="Close-up of a cream and rust veined raw granite slab" style="background:linear-gradient(135deg,#c9b393,#9c7650,#d8c6a8)"></div>
    <h3>GRANITE RAW SLABS</h3>
    <p>Sed ut perspiciatis unde omnis iste natus error sit voluptatem accusantium doloremq ue laudantium, totam rem eaque ipsa quae ab illo inventore veritatis</p>
    <a href="#">Read more &nbsp;»</a>
  </article>
  <article class="card abs" style="left:504px">
    <div class="card-photo" role="img" aria-label="Grid of granite tile samples in gold, blue and rose tones" style="background:linear-gradient(#a8875c 0 50%,#5a6f92 50%)"></div>
    <h3>GRANITE TILES</h3>
    <p>Sed ut perspiciatis unde omnis iste natus error sit voluptatem accusantium doloremq ue laudantium, totam rem eaque ipsa quae ab illo inventore veritatis</p>
    <a href="#">Read more &nbsp;»</a>
  </article>
</section>

<section>
  <div class="clients abs"></div>
  <h2 class="section-title abs" style="left:96px;top:910px;font-size:8.5px">OUR CLIENTS</h2>
  <svg class="abs" style="left:412px;top:906px" width="25" height="11" viewBox="0 0 25 11"><rect width="11" height="11" fill="#c8c8c8"/><rect x="14" width="11" height="11" fill="#c8c8c8"/><path d="M7 3 4 5.5 7 8M18 3l3 2.5L18 8" stroke="#fff" fill="none" stroke-width="1.4"/></svg>
  <span class="client abs" style="left:98px;top:944px">Delta Ridge College</span>
  <span class="client abs" style="left:240px;top:944px">Norvale</span>
  <span class="client abs" style="left:330px;top:944px">Brightline Power</span>
  <h2 class="section-title abs" style="left:511px;top:904px;font-size:8px">CERTIFIED BY NSQA &amp; MSCB</h2>
  <div class="cert-badge abs" style="left:518px;top:922px"></div>
  <div class="cert-badge abs" style="left:585px;top:922px"></div>
</section>

<footer>
  <div class="site-footer abs"></div>
  <h3 class="foot-head abs" style="left:96px;top:1006px">NAVIGATION</h3>
  <ul class="foot-list abs" style="left:97px;top:1027px">
    <li><a class="current" href="#">Home</a></li><li><a href="#">About Us</a></li><li><a href="#">Granite Tiles</a></li><li><a href="#">Granite Slabs</a></li><li><a href="#">Deliver</a></li><li><a href="#">Contact Us</a></li>
  </ul>
  <h3 class="foot-head abs" style="left:226px;top:1006px">PRODUCTS</h3>
  <ul class="foot-list products-list abs" style="left:227px;top:1026px">
    <li><a href="#">Granite Slabs</a></li><li><a href="#">Granite Tiles</a></li><li><a href="#">Raw Slabs</a></li><li><a href="#">Pre Fabs</a></li>
  </ul>
  <h3 class="foot-head abs" style="left:403px;top:1004px">CONTACTS</h3>
  <div class="field abs" style="left:405px;top:1028px">Name</div>
  <div class="field abs" style="left:405px;top:1059px">Email</div>
  <div class="field abs" style="left:405px;top:1089px">Website</div>
  <div class="field abs" style="left:556px;top:1028px;height:87px">Message</div>
  <span class="submit abs">Submit</span>

  <div class="bottom-bar abs">COPYRIGHT 2013. ALL RIGHTS RESERVED.<br>TERMS &amp; CONDITIONS &nbsp;- &nbsp;PRIVACY &nbsp;- &nbsp;DISCLAIMER</div>
  <span class="social abs" style="left:601px;background:#e0702a" aria-label="Feed"></span>
  <span class="social abs" style="left:625px;background:#c2392b" aria-label="Social link"></span>
  <span class="social abs" style="left:648px;background:#3b5a9a" aria-label="Social link"></span>
  <span class="social abs" style="left:671px;background:#2b9be0" aria-label="Social link"></span>
</footer>

</body>
</html>
```